Quillmera

Business cards and core flute signage. The business is only in its infant as a 'market' business. I would like the name to be curved across the page in different colours with a bold line underneath finished with an exotic pen drawing the line. (Similar to pictures)
We are trying to reach all markets as they are designer pens and items are made as requested or they can select from already manufactured pens on display.
I have included some images of the actual pens that I make for inspiration, we are very open to your ideas and guidance if you have a specific design in mind.
If you would more pen photo options, please contact me with your email details.
Darren Talbiro
Pen Maker & Wood Turner
Ph. 0438 271 546
Target Market(s)
Generally professional customers who would use a pen for work on a daily basis
Industry/Entity Type
Business
Requirements
Must have
- Punchy and catchy styling
Nice to have
- One of my pens

```html
<!DOCTYPE html>
<html lang="en">
<head>
<meta charset="utf-8">
<title>Quillmera – Business Card &amp; Wordmark</title>
<link href="https://fonts.googleapis.com/css2?family=Open+Sans:wght@400;600&display=swap" rel="stylesheet">
<style>
  :root {
    --stage: #5a4a3c;
    --band: #000000;
    --card-base: #ddd6d8;
    --card-light: #ece8ea;
    --card-warm: #f3a23c;
    --ink: #1c1c1c;
    --accent-red: #e2313f;
    --rule: #3a3a3a;
    --mark-white: #ffffff;
  }
  * { margin: 0; padding: 0; box-sizing: border-box; }
  html, body { width: 1200px; height: 1000px; overflow: hidden; }
  body {
    font-family: "Open Sans", Arial, sans-serif;
    background: var(--stage);
    position: relative;
  }
  .card-stage {
    position: absolute; left: 0; top: 0;
    width: 1200px; height: 678px;
    background: var(--stage);
  }
  .business-card {
    position: absolute; left: 320px; top: 179px;
    width: 560px; height: 320px;
    background:
      radial-gradient(ellipse 360px 260px at 0% 0%, var(--card-warm) 0%, rgba(243,162,60,0.35) 45%, rgba(243,162,60,0) 75%),
      linear-gradient(160deg, var(--card-light), var(--card-base));
  }
  .card-name {
    position: absolute; left: 64px; top: 72px;
    font-size: 74px; font-weight: 400;
    color: var(--ink); letter-spacing: 1px;
    line-height: 1;
  }
  .card-mark-dot {
    position: absolute; left: 440px; top: 40px;
    width: 48px; height: 48px; border-radius: 50%;
    background: var(--card-warm);
  }
  .card-details {
    position: absolute; left: 270px; top: 172px;
    width: 250px;
  }
  .card-rule {
    height: 2px; background: var(--rule); margin-bottom: 6px;
  }
  .holder-name {
    font-size: 19px; font-weight: 400; color: var(--ink);
    text-transform: uppercase; letter-spacing: 0.5px; line-height: 1.1;
  }
  .holder-role {
    font-size: 17px; color: var(--accent-red); line-height: 1.2;
  }
  .holder-phone {
    margin-top: 8px; font-size: 17px; color: var(--ink);
  }
  .holder-phone .label { color: var(--accent-red); }

  .wordmark-band {
    position: absolute; left: 0; top: 678px;
    width: 1200px; height: 322px;
    background: var(--band);
    display: flex; align-items: center; justify-content: center;
    gap: 28px;
  }
  .wordmark-name {
    font-size: 130px; font-weight: 400; color: var(--mark-white);
    line-height: 1; letter-spacing: 2px;
  }
  .wordmark-dot {
    width: 70px; height: 70px; border-radius: 50%;
    background: var(--mark-white);
  }
</style>
</head>
<body>
  <section class="card-stage">
    <article class="business-card">
      <div class="card-name">Quillmera</div>
      <div class="card-mark-dot"></div>
      <div class="card-details">
        <div class="card-rule"></div>
        <p class="holder-name">Darren Talbiro</p>
        <p class="holder-role">Pen maker &amp; wood turner</p>
        <p class="holder-phone"><span class="label">Phone:</span> 0438 271 546</p>
      </div>
    </article>
  </section>

  <section class="wordmark-band">
    <span class="wordmark-name">Quillmera</span>
    <span class="wordmark-dot"></span>
  </section>
</body>
</html>
```